Logo for Internal Medicine practice

I want a logo for my Internal Medicine practice, I would like it to be with my name on it which is Lucía Barrenechea Ruiz.

I would like the business card to say the following (it is in Spanish since my practice is in Spanish):

Lucía Barrenechea Ruiz
Medicina Interna
Cel. 5583617204
luciabarrenechearuiz@correovela.mx

Logo Text

Lucía Barrenechea

```html
<!DOCTYPE html>
<html lang="es">
<head>
<meta charset="utf-8">
<title>Lucía Barrenechea — Tarjeta de presentación</title>
<link rel="stylesheet" href="https://fonts.googleapis.com/css2?family=Nunito:wght@700;800&family=Roboto:wght@400&display=swap">
<style>
  :root {
    --backdrop: #272727;
    --card-white: #ffffff;
    --tint-light: #e6f1fa;
    --brand-blue: #1a73c8;
    --brand-blue-light: #2a8fd8;
    --brand-blue-deep: #0b6ab0;
    --ink: #222222;
    --rule: #9a9a9a;
  }
  * { margin: 0; padding: 0; box-sizing: border-box; }
  html, body {
    width: 1065px;
    height: 1200px;
    overflow: hidden;
    background: var(--backdrop);
  }
  .canvas {
    position: relative;
    width: 1065px;
    height: 1200px;
  }

  /* Front card */
  .card-front {
    position: absolute;
    left: 292px;
    top: 218px;
    width: 583px;
    height: 362px;
    border-radius: 0 181px 181px 0;
    background: linear-gradient(100deg, var(--card-white) 30%, var(--tint-light) 100%);
    box-shadow: 3px 4px 6px rgba(0,0,0,0.55);
    overflow: hidden;
  }
  .brand-square {
    position: absolute;
    left: 56px;
    top: 140px;
    width: 86px;
    height: 86px;
    background: var(--brand-blue);
  }
  .brand-vertical {
    position: absolute;
    left: 169px;
    top: 309px;
    transform-origin: 0 0;
    transform: rotate(-90deg);
    font-family: "Nunito", sans-serif;
    font-weight: 800;
    font-size: 27px;
    line-height: 30px;
    color: var(--brand-blue);
    white-space: nowrap;
  }
  .divider {
    position: absolute;
    left: 215px;
    top: 122px;
    width: 1px;
    height: 117px;
    background: var(--rule);
  }
  .details {
    position: absolute;
    left: 233px;
    top: 116px;
  }
  .full-name {
    font-family: "Nunito", sans-serif;
    font-weight: 800;
    font-size: 20px;
    line-height: 24px;
    color: var(--brand-blue);
    white-space: nowrap;
  }
  .specialty {
    font-family: "Roboto", sans-serif;
    font-size: 16px;
    line-height: 18px;
    color: var(--ink);
  }
  .contact-list {
    list-style: none;
    margin-top: 40px;
    font-family: "Roboto", sans-serif;
    font-size: 15px;
    line-height: 22px;
    color: var(--ink);
  }
  .contact-list li {
    display: flex;
    align-items: center;
    gap: 5px;
    white-space: nowrap;
  }
  .contact-icon { width: 16px; height: 16px; flex: none; }

  /* Back card */
  .card-back {
    position: absolute;
    left: 263px;
    top: 623px;
    width: 582px;
    height: 363px;
    border-radius: 181px 0 0 181px;
    background: linear-gradient(110deg, var(--brand-blue-light) 0%, var(--brand-blue-deep) 70%, #136fb4 100%);
    box-shadow: 3px 4px 6px rgba(0,0,0,0.55);
    overflow: hidden;
  }
  .brand-dot {
    position: absolute;
    left: 263px;
    top: 110px;
    width: 56px;
    height: 56px;
    border-radius: 50%;
    background: var(--card-white);
  }
  .brand-name {
    position: absolute;
    left: 0;
    right: 0;
    top: 235px;
    text-align: center;
    font-family: "Nunito", sans-serif;
    font-weight: 800;
    font-size: 40px;
    line-height: 44px;
    color: var(--card-white);
    white-space: nowrap;
  }
</style>
</head>
<body>
<main class="canvas">
  <section class="card-front" aria-label="Tarjeta, cara frontal">
    <div class="brand-square"></div>
    <div class="brand-vertical">Lucía Barrenechea</div>
    <div class="divider"></div>
    <div class="details">
      <h1 class="full-name">Lucía Barrenechea Ruiz</h1>
      <p class="specialty">Medicina Interna</p>
      <ul class="contact-list">
        <li>
          <svg class="contact-icon" viewBox="0 0 24 24" aria-hidden="true">
            <path fill="#1a73c8" d="M6.6 10.8a15.1 15.1 0 0 0 6.6 6.6l2.2-2.2a1 1 0 0 1 1-.25 11.4 11.4 0 0 0 3.6.57 1 1 0 0 1 1 1V20a1 1 0 0 1-1 1A17 17 0 0 1 3 4a1 1 0 0 1 1-1h3.5a1 1 0 0 1 1 1c0 1.25.2 2.45.57 3.57a1 1 0 0 1-.25 1z"/>
            <path fill="none" stroke="#1a73c8" stroke-width="1.8" d="M14 3.5a7 7 0 0 1 6.5 6.5M14 7a3.5 3.5 0 0 1 3 3"/>
          </svg>
          <span>5583617204</span>
        </li>
        <li>
          <svg class="contact-icon" viewBox="0 0 24 24" aria-hidden="true">
            <rect x="1" y="5" width="22" height="14" fill="#1a73c8"/>
            <path d="M1 5l11 8 11-8M1 19l8-7M23 19l-8-7" fill="none" stroke="#ffffff" stroke-width="1.4"/>
          </svg>
          <span>luciabarrenechearuiz@correovela.mx</span>
        </li>
      </ul>
    </div>
  </section>

  <section class="card-back" aria-label="Tarjeta, cara posterior">
    <div class="brand-dot"></div>
    <p class="brand-name">Lucía Barrenechea</p>
  </section>
</main>
</body>
</html>
```